Criação de Capa para Facebook para Advocacia e Direito
" assessoria e consultoria juridica ADVOCACIA GERAL gestão patrimonial e sucessório acessoria jurídica para participação de licitação, certidoes, realização de recursos, contrarazoes entre outros gestão de contratos com empresa privada e pública, elaboração de ofícios, defesas, contrarazoes. implantação e acompanhamento de normas e procedimentos para gestão de passivo trabalhista orientações sobre as alterações trazidas pela reforma trabalhista "

```html
<!DOCTYPE html>
<html lang="pt-BR">
<head>
<meta charset="UTF-8">
<title>Souza Martins – Capa</title>
<link href="https://fonts.googleapis.com/css2?family=Cinzel:wght@400&family=Montserrat:wght@400;700&display=swap" rel="stylesheet">
<style>
  :root {
    --bg: #ecebe8;
    --wine-dark: #5e0c10;
    --wine: #8a171b;
    --wine-light: #a1262a;
    --gold: #d3ae66;
    --gold-light: #f0d79a;
    --gold-dark: #a8803b;
    --ink-white: #ffffff;
  }
  * { margin: 0; padding: 0; box-sizing: border-box; }
  html, body { width: 1200px; height: 1200px; overflow: hidden; background: var(--bg); }
  .canvas { position: relative; width: 1200px; height: 1200px; }

  .cover {
    position: absolute; left: 50px; top: 240px; width: 1100px; height: 407px;
    background: linear-gradient(100deg, var(--wine-dark) 0%, var(--wine) 40%, var(--wine-light) 100%);
    overflow: hidden;
  }
  .cover-photo {
    position: absolute; left: 330px; top: 0; width: 560px; height: 407px;
    background: radial-gradient(ellipse at 45% 45%, rgba(40,5,6,0.75) 0%, rgba(70,10,12,0.45) 45%, rgba(138,23,27,0) 75%);
  }
  .gold-band {
    position: absolute; left: 0; top: 0; width: 14px; height: 407px;
    background: linear-gradient(180deg, var(--gold-light), var(--gold-dark));
  }

  .brand {
    position: absolute; left: 470px; top: 80px; width: 480px;
    display: flex; flex-direction: column; align-items: center; color: var(--ink-white);
  }
  .brand-mark {
    width: 46px; height: 46px; border: 3px solid var(--gold); margin-bottom: 26px;
  }
  .brand-name {
    font-family: "Cinzel", serif; font-size: 48px; letter-spacing: 2px; line-height: 1;
  }
  .brand-tagline {
    font-family: "Cinzel", serif; font-size: 20px; letter-spacing: 7px; margin-top: 10px;
  }

  .services {
    position: absolute; left: 430px; top: 305px; width: 640px;
    font-family: "Montserrat", sans-serif; font-weight: 700; font-size: 10.5px;
    color: var(--ink-white); letter-spacing: 0.3px;
    display: flex; flex-direction: column; align-items: center; gap: 8px;
  }
  .services ul { list-style: none; display: flex; gap: 16px; }
  .services li { display: flex; align-items: center; gap: 5px; }
  .services svg { width: 10px; height: 10px; }

  .profile {
    position: absolute; left: 50px; top: 690px; width: 280px; height: 280px;
    background: linear-gradient(135deg, var(--wine) 0%, var(--wine-dark) 100%);
    display: flex; flex-direction: column; align-items: center; justify-content: center;
    color: var(--ink-white);
  }
  .profile .brand-mark { width: 56px; height: 56px; margin-bottom: 22px; }
  .profile .brand-name { font-size: 26px; letter-spacing: 1px; }
  .profile .brand-tagline { font-size: 11px; letter-spacing: 4px; margin-top: 6px; }
</style>
</head>
<body>
<div class="canvas">
  <section class="cover">
    <div class="cover-photo" role="img" aria-label="Fotografia de um martelo de juiz sobre base de madeira, em tons escuros de vinho"></div>
    <div class="gold-band"></div>

    <div class="brand">
      <div class="brand-mark"></div>
      <div class="brand-name">Souza Martins</div>
      <div class="brand-tagline">Assessoria Jurídica</div>
    </div>

    <div class="services">
      <ul>
        <li><svg viewBox="0 0 10 10"><path d="M1 5.5 L4 8 L9 2" fill="none" stroke="#fff" stroke-width="1.6"/></svg>ADMINISTRATIVO</li>
        <li><svg viewBox="0 0 10 10"><path d="M1 5.5 L4 8 L9 2" fill="none" stroke="#fff" stroke-width="1.6"/></svg>CIVIL</li>
        <li><svg viewBox="0 0 10 10"><path d="M1 5.5 L4 8 L9 2" fill="none" stroke="#fff" stroke-width="1.6"/></svg>EMPRESARIAL</li>
        <li><svg viewBox="0 0 10 10"><path d="M1 5.5 L4 8 L9 2" fill="none" stroke="#fff" stroke-width="1.6"/></svg>FAMÍLIA</li>
        <li><svg viewBox="0 0 10 10"><path d="M1 5.5 L4 8 L9 2" fill="none" stroke="#fff" stroke-width="1.6"/></svg>IMOBILIÁRIO</li>
      </ul>
      <ul>
        <li><svg viewBox="0 0 10 10"><path d="M1 5.5 L4 8 L9 2" fill="none" stroke="#fff" stroke-width="1.6"/></svg>SUCESSÓRIO</li>
        <li><svg viewBox="0 0 10 10"><path d="M1 5.5 L4 8 L9 2" fill="none" stroke="#fff" stroke-width="1.6"/></svg>TRABALHISTA</li>
        <li><svg viewBox="0 0 10 10"><path d="M1 5.5 L4 8 L9 2" fill="none" stroke="#fff" stroke-width="1.6"/></svg>ASSESSORIA E CONSULTORIA JURÍDICA</li>
      </ul>
    </div>
  </section>

  <section class="profile">
    <div class="brand-mark"></div>
    <div class="brand-name">Souza Martins</div>
    <div class="brand-tagline">ASSESSORIA JURÍDICA</div>
  </section>
</div>
</body>
</html>
```